Letterhead LOGO and Business Card

Two Projects
1. Logo
2. Logo with Name - Brackley Asset Management for letterhead/business card
This startup is a traditional money manager that offers great value to its clients through professional money management at a very attractive fee structure.

Possible thought/concept 1: Strength, Financial Security/Integrity
Possible layout: Square logo with dark green border (back of $1 bill green), embossed lines like on $1bill (Fairbrook's forehead) in green in relief in background, gold leaf W centered in square (see Corvane Logo) with 5 point stars above the points of the W.
Possible thought/concept 2: Some iteration of a globe and the capital letter W - superimposed, cut-out, etc. This business will have a global presence.
Concept 3: I am not sure if Concept 1 can be blended with Concept 2, but someone out there may be crafty enough to blend the two concepts. If so, make sure China and the US are represented..

Business

W

```html
<!DOCTYPE html>
<html lang="en">
<head>
<meta charset="utf-8">
<title>Brackley Asset Management – Identity</title>
<link rel="stylesheet" href="https://fonts.googleapis.com/css2?family=EB+Garamond:wght@500&family=Open+Sans:wght@400;600&display=swap">
<style>
  :root {
    --green: #214434;
    --gold: #825a16;
    --white: #ffffff;
    --paper: #ffffff;
    --faint: #f1f4f2;
    --rule: #d9dcda;
    --serif: "EB Garamond", Georgia, serif;
    --sans: "Open Sans", Arial, sans-serif;
  }
  * { box-sizing: border-box; margin: 0; padding: 0; }
  html, body { width: 1091px; height: 1200px; overflow: hidden; background: var(--white); }
  .canvas { position: relative; width: 1091px; height: 1200px; background: var(--white); }

  /* wordmark */
  .mark { position: absolute; display: flex; flex-direction: column; align-items: center; font-family: var(--serif); font-weight: 500; color: var(--green); line-height: 1; }
  .mark--left { align-items: flex-start; }
  .mark--light { color: var(--white); }
  .mark-square { width: 1.9em; height: 1.9em; background: currentColor; margin-bottom: .55em; }
  .mark-name { font-size: 1em; letter-spacing: .28em; margin-right: -.28em; }
  .mark-sub { font-size: .46em; letter-spacing: .36em; margin-right: -.36em; margin-top: .45em; }

  .divider { position: absolute; left: 0; top: 348px; width: 1080px; height: 4px; background: linear-gradient(#e4e6e5, #f7f7f7); }

  .card { position: absolute; width: 389px; height: 223px; overflow: hidden; box-shadow: 0 2px 10px rgba(0,0,0,.12); }
  .card--white { background: var(--paper); }
  .card--gold { background: var(--gold); }
  .card--green { background: var(--green); }

  .faint-disc { position: absolute; border-radius: 50%; background: var(--faint); }

  .card-name { position: absolute; left: 295px; top: 104px; font: 400 12px var(--sans); color: var(--green); }
  .card-band { position: absolute; left: 0; top: 122px; width: 100%; height: 21px; background: var(--gold); }
  .card-position { position: absolute; left: 295px; top: 3px; font: 400 12px var(--sans); color: var(--white); }
  .card-contact { position: absolute; left: 0; top: 143px; width: 100%; height: 80px; background: var(--green); }
  .contact-line { position: absolute; display: flex; align-items: center; gap: 6px; font: 400 8.5px var(--sans); color: var(--white); white-space: nowrap; }
  .contact-line svg { width: 9px; height: 9px; flex: none; }
  .card-rule { position: absolute; left: 0; bottom: 0; width: 100%; height: 3px; background: var(--green); }

  .sheet { position: absolute; background: var(--paper); box-shadow: 0 2px 14px rgba(0,0,0,.1); }
  .sheet--back { left: 470px; top: 398px; width: 588px; height: 748px; transform: rotate(-.4deg); }
  .sheet--front { left: 466px; top: 404px; width: 589px; height: 744px; overflow: hidden; }
  .sheet-rule { position: absolute; left: 148px; top: 86px; width: 390px; height: 1px; background: var(--gold); }
  .sheet-band { position: absolute; left: 6px; bottom: 0; width: 583px; height: 40px; background: var(--green); transform: rotate(-.4deg); transform-origin: left bottom; }
  .sheet .contact-line { font-size: 6.5px; color: var(--green); gap: 5px; }
  .sheet .contact-line svg { width: 7px; height: 7px; }
</style>
</head>
<body>
<main class="canvas">

  <!-- Primary wordmark -->
  <div class="mark" style="left:0; width:1091px; top:40px; font-size:54px;">
    <span class="mark-square"></span>
    <span class="mark-name">BRACKLEY</span>
    <span class="mark-sub">ASSET MANAGEMENT</span>
  </div>

  <div class="divider"></div>

  <!-- Business card front -->
  <section class="card card--white" style="left:30px; top:413px;">
    <span class="faint-disc" style="left:210px; top:-30px; width:170px; height:170px;"></span>
    <div class="mark mark--left" style="left:18px; top:22px; font-size:23px;">
      <span class="mark-name">BRACKLEY</span>
      <span class="mark-sub">ASSET MANAGEMENT</span>
    </div>
    <p class="card-name">your name</p>
    <div class="card-band"><p class="card-position">position</p></div>
    <div class="card-contact">
      <p class="contact-line" style="left:45px; top:16px;">
        <svg viewBox="0 0 10 10"><path d="M5 0a3.5 3.5 0 0 0-3.5 3.5C1.5 6 5 10 5 10s3.5-4 3.5-6.5A3.5 3.5 0 0 0 5 0zm0 5a1.5 1.5 0 1 1 0-3 1.5 1.5 0 0 1 0 3z" fill="#fff"/></svg>your address, address 1</p>
      <p class="contact-line" style="left:60px; top:33px;">your address, address 2</p>
      <p class="contact-line" style="left:45px; top:49px;">
        <svg viewBox="0 0 10 10"><circle cx="5" cy="5" r="4.3" fill="none" stroke="#fff" stroke-width="1.2"/><path d="M1 5h8M5 .7c-2 2.5-2 6.1 0 8.6M5 .7c2 2.5 2 6.1 0 8.6" fill="none" stroke="#fff" stroke-width=".8"/></svg>www.yourwebsite.com</p>
      <p class="contact-line" style="left:218px; top:16px;">
        <svg viewBox="0 0 10 10"><path d="M3 1l2 2-1 1c.5 1 1 1.5 2 2l1-1 2 2-1.5 1.5C5 8 2 5 1.5 2.5z" fill="#fff"/></svg>+(000) 1234 5678</p>
      <p class="contact-line" style="left:218px; top:33px;">
        <svg viewBox="0 0 10 10"><rect x="2.5" y="1" width="5" height="3" fill="none" stroke="#fff"/><rect x="1" y="4" width="8" height="5" fill="none" stroke="#fff"/></svg>+(000) 1234 5678</p>
      <p class="contact-line" style="left:218px; top:49px;">
        <svg viewBox="0 0 10 10"><rect x="1" y="2" width="8" height="6" fill="none" stroke="#fff"/><path d="M1 2l4 3.5L9 2" fill="none" stroke="#fff"/></svg>name@emailaddress.com</p>
    </div>
  </section>

  <!-- Business card back, white -->
  <section class="card card--white" style="left:30px; top:665px;">
    <div class="mark" style="left:0; width:389px; top:60px; font-size:21px;">
      <span class="mark-square"></span>
      <span class="mark-name">BRACKLEY</span>
      <span class="mark-sub">ASSET MANAGEMENT</span>
    </div>
    <span class="card-rule"></span>
  </section>

  <!-- Business card back, gold -->
  <section class="card card--gold" style="left:30px; top:916px;">
    <div class="mark mark--light" style="left:0; width:389px; top:60px; font-size:21px;">
      <span class="mark-square"></span>
      <span class="mark-name">BRACKLEY</span>
      <span class="mark-sub">ASSET MANAGEMENT</span>
    </div>
  </section>

  <!-- Letterhead -->
  <div class="sheet sheet--back"></div>
  <section class="sheet sheet--front">
    <span class="faint-disc" style="left:160px; top:280px; width:300px; height:300px;"></span>
    <div class="mark" style="left:52px; top:30px; font-size:11px;">
      <span class="mark-square"></span>
      <span class="mark-name">BRACKLEY</span>
      <span class="mark-sub">ASSET MANAGEMENT</span>
    </div>
    <span class="sheet-rule"></span>
    <p class="contact-line" style="left:358px; top:55px;">
      <svg viewBox="0 0 10 10"><path d="M3 1l2 2-1 1c.5 1 1 1.5 2 2l1-1 2 2-1.5 1.5C5 8 2 5 1.5 2.5z" fill="#214434"/></svg>+(000) 1234 5678</p>
    <p class="contact-line" style="left:358px; top:69px;">
      <svg viewBox="0 0 10 10"><rect x="2.5" y="1" width="5" height="3" fill="#825a16"/><rect x="1" y="4" width="8" height="5" fill="#825a16"/></svg>+(000) 1234 5678</p>
    <p class="contact-line" style="left:451px; top:55px;">
      <svg viewBox="0 0 10 10"><path d="M5 0a3.5 3.5 0 0 0-3.5 3.5C1.5 6 5 10 5 10s3.5-4 3.5-6.5A3.5 3.5 0 0 0 5 0zm0 5a1.5 1.5 0 1 1 0-3 1.5 1.5 0 0 1 0 3z" fill="#825a16"/></svg>your address, address 1</p>
    <p class="contact-line" style="left:451px; top:69px;">
      <svg viewBox="0 0 10 10"><circle cx="5" cy="5" r="4.3" fill="none" stroke="#825a16" stroke-width="1.2"/><path d="M1 5h8M5 .7c-2 2.5-2 6.1 0 8.6M5 .7c2 2.5 2 6.1 0 8.6" fill="none" stroke="#825a16" stroke-width=".8"/></svg>www.yourwebsite.com</p>
    <span class="sheet-band"></span>
  </section>

  <!-- Business card back, green -->
  <section class="card card--green" style="left:457px; top:808px; width:390px;">
    <div class="mark mark--light" style="left:0; width:390px; top:60px; font-size:22px;">
      <span class="mark-square"></span>
      <span class="mark-name">BRACKLEY</span>
      <span class="mark-sub">ASSET MANAGEMENT</span>
    </div>
  </section>

</main>
</body>
</html>
```